Brightbuns Business Card Design

Our company is called Brightbuns. We manufacture confectionary snacks & frozen novelties. Our initial product portfolio includes frozen ice lollies/popsicles & stick ice cream bars.

We require a business card design.

Please use the attached Logo.

Please use an orange, brown, yellow colour code. You may choose any combination of the 3 or include all three. The logo however must remain orange.

Target Market(s)

Business card will be targeted at distributors of our products such as supermarket procurement managers, convenience store owners, wholesale distributors and merchandising agents.

Industry/Entity Type

Business

Requirements
Must have
• Kelvin Marsh_Director/ P.O.Box Westhollow 5172, Accra, Ghana / m: 00233(0)507318264/ e: kelvin.marsh@fernpost.co.uk

```html
<!DOCTYPE html>
<html lang="en">
<head>
<meta charset="utf-8">
<title>Brightbuns Business Card</title>
<link rel="stylesheet" href="https://fonts.googleapis.com/css2?family=Baloo+2:wght@600;700&display=swap">
<style>
  :root {
    --brand-orange: #f37021;
    --paper: #ffffff;
  }
  * { margin: 0; padding: 0; box-sizing: border-box; }
  html, body {
    width: 767px;
    height: 1200px;
    overflow: hidden;
    background: var(--paper);
  }
  .card {
    position: relative;
    width: 767px;
    height: 1200px;
    font-family: "Baloo 2", sans-serif;
    color: var(--brand-orange);
  }
  .card-shapes {
    position: absolute;
    inset: 0;
  }
  .brand-name {
    position: absolute;
    left: 176px;
    top: 292px;
    font-size: 74px;
    font-weight: 700;
    line-height: 1;
    letter-spacing: 0.5px;
    color: var(--brand-orange);
  }
  .contact {
    position: absolute;
    left: 245px;
    top: 556px;
    width: 423px;
    text-align: center;
    font-weight: 600;
  }
  .contact-name {
    font-size: 30px;
    line-height: 40px;
  }
  .contact-role {
    font-size: 23px;
    line-height: 34px;
    font-style: italic;
    margin-bottom: 4px;
  }
  .contact-line {
    font-size: 22px;
    line-height: 37px;
  }
  .contact-line.email {
    font-size: 21px;
  }
</style>
</head>
<body>
  <div class="card">
    <svg class="card-shapes" width="767" height="1200" viewBox="0 0 767 1200" aria-hidden="true">
      <rect class="card-frame" x="109" y="111" width="550" height="978" rx="62"
            fill="none" stroke="var(--brand-orange)" stroke-width="18"/>
      <path class="bubble-depth" fill="var(--brand-orange)"
            d="M245,515 L668,515 L668,865 L520,865 L497,978 L440,1022 L350,865 L235,865
               Q180,865 180,810 L180,590 Q180,566 200,552 Z"/>
      <path class="bubble-face" fill="var(--paper)" stroke="var(--brand-orange)" stroke-width="3"
            d="M275,517 L668,517 L668,815 L507,815 L492,950 L395,815 L278,815
               Q247,815 247,784 L247,548 Q247,517 275,517 Z"/>
    </svg>

    <div class="brand-name">Brightbuns</div>

    <div class="contact">
      <p class="contact-name">Kelvin Marsh</p>
      <p class="contact-role">Director</p>
      <p class="contact-line">P.O.Box Westhollow 5172,</p>
      <p class="contact-line">Accra, Ghana</p>
      <p class="contact-line">m: 00233(0)507318264</p>
      <p class="contact-line email">e: kelvin.marsh@fernpost.co.uk</p>
    </div>
  </div>
</body>
</html>
```